Hair extensions packaging design

Professional hair extensions packaging design.
We like a clean and crisp look. The design should convey luxury and highest quality.

Target Market(s)

women ages 16-40

Industry/Entity Type

beauty, hair

Font styles to use
Other font styles liked:
• kiona

Requirements
Must have
• clean, crisp, professional look

```html
<!DOCTYPE html>
<html lang="en">
<head>
<meta charset="utf-8">
<title>LuxeStrand Packaging Set</title>
<link href="https://fonts.googleapis.com/css2?family=Raleway:wght@300;400;500;600&display=swap" rel="stylesheet">
<style>
  :root{
    --mint:#deeddb;
    --black:#000000;
    --white:#ffffff;
    --gold:#c7a257;
    --gold-soft:#e6cf7e;
    --gold-pale:#f3e6b2;
    --ink:#1d1d1d;
    --label:#333333;
  }
  *{box-sizing:border-box;margin:0;padding:0}
  html,body{width:722px;height:1200px;overflow:hidden;background:var(--mint)}
  body{position:relative;font-family:'Raleway',sans-serif;color:var(--ink)}
  .panel{position:absolute;overflow:hidden}
  .panel--dark{background:var(--black)}
  .panel--light{background:var(--white)}
  .panel svg.frame{position:absolute;left:0;top:0;width:100%;height:100%}
  .panel-number{position:absolute;font-size:5px;color:var(--label);width:20px;text-align:center}

  .gold-bar{position:absolute;left:33px;top:0;width:135px;height:7px;
    background:linear-gradient(90deg,#e9c65a,#fff1b8 30%,#b8923d 60%,#f7e7a6 100%)}

  .wordmark{position:absolute;left:0;width:100%;text-align:center;
    font-family:'Raleway',sans-serif;font-weight:400;font-size:12px;letter-spacing:.5px;color:var(--gold)}
  .wordmark::before{content:"";display:inline-block;width:5px;height:5px;border-radius:50%;
    background:var(--gold);margin-right:5px;vertical-align:middle}

  .claim{position:absolute;left:0;width:100%;text-align:center;font-size:5.6px;line-height:8px;
    text-transform:uppercase;font-weight:400}
  .claim .guarantee{display:block;margin-top:3px}
  .panel--dark .claim{color:var(--gold-soft)}
  .panel--light .claim{color:var(--ink)}

  .web{position:absolute;left:0;width:100%;text-align:center;font-size:4.6px;letter-spacing:1px;color:var(--gold-soft)}
  .panel--light .web{color:var(--gold)}
  .web--faint{color:var(--gold-pale)!important}

  .waves{position:absolute;left:0;width:100%}
  .waves--dark{background:linear-gradient(170deg,rgba(0,0,0,0) 25%,rgba(190,155,80,.55) 55%,rgba(120,95,45,.6) 100%);
    clip-path:polygon(0 72%,30% 45%,65% 20%,100% 0,100% 100%,0 100%)}
  .waves--light{background:linear-gradient(170deg,rgba(255,255,255,0) 20%,rgba(240,214,120,.55) 55%,rgba(226,190,90,.5) 100%);
    clip-path:polygon(0 45%,30% 28%,65% 12%,100% 0,100% 100%,0 100%)}

  .copy{position:absolute;left:0;width:100%;text-align:center;padding:0 36px;color:var(--ink)}
  .copy--lead{font-weight:300;font-size:9.2px;line-height:16.6px;padding:0 40px}
  .copy--story{font-weight:400;font-size:8px;line-height:16px}
  .panel--mid .copy--story{line-height:13.9px}
  .care-title{position:absolute;left:0;width:100%;text-align:center;font-weight:600;font-size:9.6px;
    letter-spacing:2.6px;color:var(--gold)}
  .care-list{list-style:none}
  .care-list li::before{content:"";display:inline-block;width:2.5px;height:2.5px;background:var(--gold-soft);
    transform:rotate(45deg);margin-right:3px;vertical-align:middle}
  .care-list li+li{margin-top:3px}
  .panel--mid .care-list{line-height:13.9px}
  .panel--mid .care-list li+li{margin-top:3px}

  .divider{position:absolute;left:50%;transform:translateX(-50%);display:flex;gap:2px;align-items:center}
  .divider i{display:block;background:var(--gold-soft);transform:rotate(45deg)}
  .divider i:nth-child(1),.divider i:nth-child(3){width:2.4px;height:2.4px}
  .divider i:nth-child(2){width:4px;height:4px}
</style>
</head>
<body>

<!-- 1: black box lid -->
<section class="panel panel--dark" style="left:26px;top:37px;width:200px;height:200px">
  <div class="gold-bar"></div>
  <div class="wordmark" style="top:80px">LUXESTRAND</div>
  <svg class="frame" viewBox="0 0 200 200" aria-hidden="true">
    <path d="M0 186 H22 Q28 186 28 180 V156 Q28 148 36 148 H164 Q172 148 172 156 V180 Q172 186 178 186 H200" fill="none" stroke="#c7a257" stroke-width=".7"/>
  </svg>
  <p class="claim" style="top:153px">Highest quality, double<br>drawn, 100% human remi hair<span class="guarantee">Guaranteed!</span></p>
  <p class="web" style="top:189px">www.luxestrand.com</p>
</section>
<div class="panel-number" style="left:116px;top:244px">1</div>

<!-- 2: black box with waves -->
<section class="panel panel--dark" style="left:266px;top:37px;width:200px;height:200px">
  <div class="wordmark" style="top:62px">LUXESTRAND</div>
  <p class="claim" style="top:122px">Highest quality, double drawn,<br>100% human remi hair<span class="guarantee">Guaranteed!</span></p>
  <div class="waves waves--dark" role="img" aria-label="Fine gold flowing wave line pattern" style="top:145px;height:55px"></div>
  <svg class="frame" viewBox="0 0 200 200" aria-hidden="true">
    <path d="M56 200 V190 Q56 184 62 184 H138 Q144 184 144 190 V200" fill="#000" stroke="#c7a257" stroke-width=".6"/>
  </svg>
  <p class="web" style="top:187px">www.luxestrand.com</p>
</section>
<div class="panel-number" style="left:356px;top:244px">2</div>

<!-- 3: white box -->
<section class="panel panel--light" style="left:493px;top:36px;width:200px;height:200px">
  <svg class="frame" viewBox="0 0 200 200" aria-hidden="true">
    <path d="M0 33 H22 Q28 33 28 27 V19 Q28 12 36 12 H164 Q172 12 172 19 V27 Q172 33 178 33 H200" fill="none" stroke="#e6cf7e" stroke-width=".7"/>
  </svg>
  <div class="wordmark" style="top:80px">LUXESTRAND</div>
  <div class="waves waves--light" role="img" aria-label="Fine gold flowing wave line pattern" style="top:125px;height:75px"></div>
  <p class="claim" style="top:146px">Highest quality, double drawn,<br>100% human remi hair<span class="guarantee">Guaranteed!</span></p>
  <svg class="frame" viewBox="0 0 200 200" aria-hidden="true">
    <path d="M56 200 V192 Q56 186 62 186 H138 Q144 186 144 192 V200" fill="#fff" stroke="#f3e6b2" stroke-width=".6"/>
  </svg>
  <p class="web web--faint" style="top:189px">www.luxestrand.com</p>
</section>
<div class="panel-number" style="left:582px;top:247px">3</div>

<!-- 4: white box variant -->
<section class="panel panel--light" style="left:493px;top:268px;width:200px;height:200px">
  <svg class="frame" viewBox="0 0 200 200" aria-hidden="true">
    <path d="M0 33 H22 Q28 33 28 27 V19 Q28 12 36 12 H164 Q172 12 172 19 V27 Q172 33 178 33 H200" fill="none" stroke="#e6cf7e" stroke-width=".7"/>
  </svg>
  <div class="wordmark" style="top:80px">LUXESTRAND</div>
  <div class="waves waves--light" role="img" aria-label="Fine gold flowing wave line pattern" style="top:125px;height:75px"></div>
  <p class="claim" style="top:148px">Highest quality, double drawn,<br>100% human remi hair<span class="guarantee">Guaranteed!</span></p>
  <svg class="frame" viewBox="0 0 200 200" aria-hidden="true">
    <path d="M56 200 V192 Q56 186 62 186 H138 Q144 186 144 192 V200" fill="#fff" stroke="#f3e6b2" stroke-width=".6"/>
  </svg>
  <p class="web web--faint" style="top:188px">www.luxestrand.com</p>
</section>
<div class="panel-number" style="left:585px;top:479px">4</div>

<!-- tall insert card -->
<section class="panel panel--light" style="left:22px;top:272px;width:200px;height:897px">
  <svg class="frame" viewBox="0 0 200 897" aria-hidden="true">
    <path d="M0 42 H22 Q28 42 28 36 V29 Q28 21 36 21 H164 Q172 21 172 29 V36 Q172 42 178 42 H200" fill="none" stroke="#e6cf7e" stroke-width=".7"/>
  </svg>
  <p class="copy copy--lead" style="top:63px">LuxeStrand hair is cut directly from the donor to ensure the cuticle remains in tact and the hair will never tangle!</p>
  <div class="divider" style="top:207px"><i></i><i></i><i></i></div>
  <h2 class="care-title" style="top:294px">CARE INSTRUCTIONS</h2>
  <ul class="copy copy--story care-list" style="top:314px">
    <li>LuxeStrand provides only the highest in quality, human remi hair that requires very little care to maintain its luxurious feel</li>
    <li>Wash the hair with a sulfate free shampoo and follow with a moisturizing conditioner that is formulated for hair extensions</li>
  </ul>
  <div class="divider" style="top:508px"><i></i><i></i><i></i></div>
  <p class="copy copy--story" style="top:586px">We proudly show our immense passion for delivering superior quality in our full product line. LuxeStrand is strongly committed to serving their clients with utmost integrity, believing in a foundation of personal and professional ethics and our over 25 years of service in the beauty industry!</p>
  <div class="waves waves--light" role="img" aria-label="Fine gold flowing wave line pattern" style="top:752px;height:130px"></div>
  <svg class="frame" viewBox="0 0 200 897" aria-hidden="true">
    <path d="M0 880 H50 Q56 880 56 874 V869 Q56 863 62 863 H138 Q144 863 144 869 V874 Q144 880 150 880 H200" fill="none" stroke="#e6cf7e" stroke-width=".6"/>
    <rect x="57" y="864" width="86" height="16" fill="#fff"/>
  </svg>
  <p class="web" style="top:869px;color:var(--ink)">www.luxestrand.com</p>
</section>

<!-- compact insert card -->
<section class="panel panel--light panel--mid" style="left:259px;top:270px;width:200px;height:623px">
  <svg class="frame" viewBox="0 0 200 623" aria-hidden="true">
    <path d="M0 43 H22 Q28 43 28 37 V30 Q28 22 36 22 H164 Q172 22 172 30 V37 Q172 43 178 43 H200" fill="none" stroke="#c7a257" stroke-width=".7"/>
  </svg>
  <p class="copy copy--lead" style="top:65px">LuxeStrand hair is cut directly from the donor to ensure the cuticle remains in tact and the hair will never tangle!</p>
  <div class="divider" style="top:158px"><i></i><i></i><i></i></div>
  <h2 class="care-title" style="top:185px">CARE INSTRUCTIONS</h2>
  <ul class="copy copy--story care-list" style="top:203px">
    <li>LuxeStrand provides only the highest in quality, human remi hair that requires very little care to maintain its luxurious feel</li>
    <li>Wash the hair with a sulfate free shampoo and follow with a moisturizing conditioner that is formulated for hair extensions</li>
  </ul>
  <div class="divider" style="top:334px"><i></i><i></i><i></i></div>
  <p class="copy copy--story" style="top:373px">We proudly show our immense passion for delivering superior quality in our full product line. LuxeStrand is strongly committed to serving their clients with utmost integrity, believing in a foundation of personal and professional ethics and our over 25 years of service in the beauty industry!</p>
  <div class="waves waves--light" role="img" aria-label="Fine gold flowing wave line pattern" style="top:500px;height:106px"></div>
  <svg class="frame" viewBox="0 0 200 623" aria-hidden="true">
    <path d="M0 606 H50 Q56 606 56 600 V595 Q56 589 62 589 H138 Q144 589 144 595 V600 Q144 606 150 606 H200" fill="none" stroke="#c7a257" stroke-width=".6"/>
    <rect x="57" y="590" width="86" height="16" fill="#fff"/>
  </svg>
  <p class="web" style="top:595px">www.luxestrand.com</p>
</section>

</body>
</html>
```